Corvel Lending Systems Re-design.

Quillmere have recently launched a new site using Brickloft CMS system (http://www.corvellendingsystems.example.com.au). We are looking to update the look and feel to match the rest of our brands (http://www.velnarix.example.com.au and http://www.tidelark.example.com.au) We are keen for the design to be more visually engaging, incorporating more imagery and create a clean and easy to navigate interface.

We are looking for 2 pages to be designed. The first page would be the homepage which should contain the following:
Menu to the sub categories provided in the site map.
Room for latest news articles
Small area for polls
Contact us section
Page 2 should offer a content page. An example of this would be CRM (sales Platform) from the site map. This page would need to contain an overall description of the product and menu to the following:
Flash Demo.
Features and Benefits.
Enquire now.

Target Market(s)

Quillmere offer software and web tools that enable Mortgage brokers to manage their clients, choose the most applicable loan and submit applications to the lender (bank).
The target market for this site is mainly mortgage brokers and the banking industry (lenders, Brokerages and Aggregators of homeloans).
Mortgage brokers often work in small brokerages or are self employed running their business within the local community, alternatively they may own a franchise business such as Brindle Key Finance, ZOLT or Lender Harbour.

Industry/Entity Type

Software

Number of Pages Required

2 pages

Requirements
Must have
• Must suitably match the look and feel of our sister companies velnarix.example.com.au and tidelark.example.com.au and our group site corvelgroup.example.com.au.
Colour scheme should not differ from the base logo colours provided.
Should not have
• Although Quillmere offers mortgage software to brokers we do not sell homeloans or deal directly with buyers, therefore pictures of houses and a look you see from lenders is not what we are looking for. Our customers are Mortgage brokers and top tier banks.

```html
<!DOCTYPE html>
<html lang="en">
<head>
<meta charset="utf-8">
<title>Quillmere Group – Product</title>
<link href="https://fonts.googleapis.com/css2?family=Arimo:ital,wght@0,400;0,700;1,700&family=PT+Sans+Narrow:wght@700&family=PT+Sans:wght@400&display=swap" rel="stylesheet">
<style>
:root{
  --brand-red:#9b0000;
  --brand-crimson:#b3123e;
  --nav-active:#9a9fc4;
  --text:#222;
  --muted:#555;
  --meta:#999;
  --rule:#d4d4d4;
  --sheet:#fbfbfb;
}
*{box-sizing:border-box;margin:0;padding:0}
html,body{width:1132px;height:1200px;overflow:hidden}
body{
  position:relative;
  font-family:"Arimo",Arial,sans-serif;
  color:var(--text);
  background:linear-gradient(180deg,#f4f4f4 0%,#dcdcdc 60%,#c8c8c8 100%);
}
.sheet{
  position:absolute;left:94px;top:20px;width:942px;height:1170px;
  background:linear-gradient(180deg,#e9e9e9 0,#f7f7f7 140px,var(--sheet) 160px);
  border:1px solid #bdbdbd;
}
.brand{
  position:absolute;left:34px;top:22px;
  font-weight:700;font-size:40px;letter-spacing:-1px;color:var(--brand-crimson);
  display:flex;align-items:center;gap:8px;
}
.brand-dot{width:14px;height:14px;border-radius:50%;background:var(--brand-crimson)}
.nav{
  position:absolute;left:35px;top:98px;width:890px;height:31px;
  background:var(--brand-red);display:flex;list-style:none;
  font-family:"PT Sans",Arial,sans-serif;font-size:12.5px;
}
.nav li{color:#fff;line-height:31px;text-align:center;position:relative;white-space:nowrap;flex:none}
.nav li.active{background:var(--nav-active)}
.nav li.active::after{
  content:"";position:absolute;left:50%;bottom:-7px;margin-left:-7px;
  border:7px solid transparent;border-bottom:0;border-top-color:var(--nav-active)}
.content{
  position:absolute;left:35px;top:157px;width:890px;height:868px;
  background:#fafafa;border:1px solid var(--rule);display:flex;
}
.main{width:610px;padding:10px 18px 0 18px;border-right:1px solid var(--rule)}
.side{flex:1;padding:22px 28px 0 28px}
h1,.sec-title,.prod-title{font-family:"PT Sans Narrow","Arial Narrow",sans-serif;font-weight:700;color:var(--brand-red)}
h1{font-size:24px;margin-bottom:4px}
.demo{
  width:571px;height:248px;background:#000;border:3px solid #8c8c8c;
  display:flex;align-items:center;justify-content:center;
  font-weight:700;font-size:29px;color:#2a2a2a;letter-spacing:.5px;
}
.main p{font-size:12.2px;line-height:17px;margin-top:18px}
.main p em{font-weight:700}
.sec-head{
  position:relative;margin-top:18px;height:31px;
  border:1px solid #ddd;background:linear-gradient(180deg,#fff,#f0f0f0);
  padding-left:8px;
}
.sec-head::before{content:"";position:absolute;left:0;top:4px;bottom:4px;width:2px;background:var(--brand-red)}
.sec-head::after{content:"";position:absolute;left:14px;bottom:-6px;border:6px solid transparent;border-bottom:0;border-top-color:#e6e6e6}
.sec-title{font-size:17px;line-height:31px}
.indent{padding-left:20px}
.indent p{margin-top:16px}
.ticks{list-style:none;margin:10px 0 0 30px;font-size:12.2px;font-weight:700;line-height:17px}
.ticks li{position:relative;padding-left:16px;margin-bottom:8px}
.ticks svg{position:absolute;left:0;top:3px}
.pill{
  display:inline-block;font-size:9.5px;color:#666;height:17px;line-height:17px;
  padding:0 12px;border-radius:9px;
  background:linear-gradient(180deg,#f2f2f2,#c8c8c8);border:1px solid #bdbdbd;
}
.pill::after{content:" \203A";}
.prod{position:relative;padding-left:29px;margin-bottom:20px}
.prod svg{position:absolute;left:0;top:0}
.prod-title{font-size:13.5px;line-height:16px;max-width:168px}
.prod p{font-size:10.5px;color:var(--muted);line-height:13px;margin:7px 0 8px;max-width:195px}
.side .sec-head{margin:22px 0 0 0;height:30px}
.side .sec-title{font-size:17px;line-height:30px}
.news{padding:14px 10px 0}
.news h3{font-size:12.5px;font-weight:700;color:#333}
.news .date{font-size:9.5px;color:var(--meta)}
.news p{font-size:10.5px;line-height:17px;margin-top:16px}
.right{text-align:right;margin-top:6px}
.poll{padding:14px 10px 0;font-size:10.5px;line-height:17px}
.poll label{display:flex;align-items:center;gap:6px;margin-left:10px;font-size:11px}
.radio{width:11px;height:11px;border-radius:50%;border:1px solid #888;background:linear-gradient(#fff,#ddd)}
.footer{
  position:absolute;left:35px;top:1050px;width:890px;height:89px;
  background:var(--brand-red);color:#fff;text-align:center;font-size:11px;
}
.footer .office{margin-top:18px}
.footer .links{margin-top:12px;font-weight:700}
.footer .copy{margin-top:1px}
</style>
</head>
<body>
<div class="sheet">
  <div class="brand"><span>Quillmere</span><span class="brand-dot"></span></div>

  <ul class="nav">
    <li class="active" style="width:85px">Home</li><li style="width:140px">Mortgage Solutions</li><li style="width:104px">Messaging</li><li style="width:90px">Company</li><li style="width:78px">News</li><li style="width:96px">Support</li><li style="width:84px">Privacy Policy</li><li style="width:120px">Site Map</li><li style="width:93px">Contact Us</li>
  </ul>

  <div class="content">
    <main class="main">
      <h1>Product Name</h1>
      <div class="demo">FLASH DEMO</div>
      <p><em>Product description.</em> Lorem ipsum dolor sit amet, consectetur adipiscing elit. Sed sodales purus sed mauris scelerisque sit amet scelerisque turpis convallis. Proin mattis tincidunt metus eu consectetur. Quisque elit ante, feugiat ac vulputate nec, suscipit vel est. Vivamus laoreet condimentum tortor at mollis. Proin tempus velit nec libero imperdiet dapibus et in augue. Vestibulum vitae aliquet urna. Nulla egestas facilisis magna sed tempor. Curabitur ligula sem, tristique eu facilisis et, pharetra iaculis ligula. Suspendisse mauris risus, suscipit a pellentesque quis, venenatis a mauris. Duis vestibulum nunc vel purus pretium quis suscipit enim tempor.</p>
      <p>Maecenas volutpat felis vel eros tincidunt suscipit. In hac habitasse platea dictumst. Sed nec sapien erat, in bibendum elit. Etiam nulla augue, tempor id cursus vitae, lacinia at magna. Curabitur lobortis enim eu nisi consectetur vitae pharetra velit hendrerit.</p>
      <div class="sec-head"><h2 class="sec-title">Features and Benefits</h2></div>
      <div class="indent">
        <p>Vestibulum a est lorem, ut hendrerit dolor. Praesent eu augue ut tellus euismod molestie vitae vehicula turpis. Nam pulvinar tellus et augue feugiat at cursus erat hendrerit. Pellentesque congue molestie semper. Ut aliquet, eros et viverra tempus, nulla dolor iaculis tortor, eget lacinia leo quam id mi. Phasellus fermentum ultricies risus ut lobortis. Duis rhoncus elementum porta. Proin velit est, porta vitae pellentesque a, tincidunt ac turpis. Mauris congue mauris a erat commodo malesuada. Fusce feugiat sodales elementum.</p>
        <ul class="ticks">
          <li><svg width="11" height="10" viewBox="0 0 11 10"><path d="M1 5l3 3 6-7" fill="none" stroke="#222" stroke-width="2.2"/></svg>Curabitur scelerisque rhoncus nisi ut fermentum. In auctor commodo purus vitae tempus.</li>
          <li><svg width="11" height="10" viewBox="0 0 11 10"><path d="M1 5l3 3 6-7" fill="none" stroke="#222" stroke-width="2.2"/></svg>Aliquam purus urna, lobortis et vehicula et, tincidunt sit amet magna.</li>
          <li><svg width="11" height="10" viewBox="0 0 11 10"><path d="M1 5l3 3 6-7" fill="none" stroke="#222" stroke-width="2.2"/></svg>Praesent porta, mi ut sodales sodales, sem ligula mollis eros, vitae lobortis nisl quam posuere leo.</li>
        </ul>
        <span class="pill" style="margin-left:26px">enquire now</span>
      </div>
    </main>

    <aside class="side">
      <div class="prod">
        <svg width="22" height="22" viewBox="0 0 22 22"><rect x="2" y="2" width="18" height="18" rx="2" fill="#d9a441"/><circle cx="11" cy="12" r="6" fill="#eee" stroke="#999"/><circle cx="11" cy="12" r="1.5" fill="#999"/></svg>
        <div class="prod-title">CRM (Sales Platform)</div>
        <p>Lorem ipsum dolor sit amet, consectetur adipiscing elit. Sed sodales purus sed mauris scelerisque sit.</p>
        <span class="pill">learn more</span>
      </div>
      <div class="prod">
        <svg width="22" height="22" viewBox="0 0 22 22"><path d="M4 10a7 7 0 0 1 13-3" fill="none" stroke="#3a78c4" stroke-width="2.5"/><path d="M18 12a7 7 0 0 1-13 3" fill="none" stroke="#3a78c4" stroke-width="2.5"/><path d="M15 3l3 4-5 1z" fill="#3a78c4"/><path d="M7 19l-3-4 5-1z" fill="#3a78c4"/></svg>
        <div class="prod-title">Commission Processing</div>
        <p>Praesent eu augue ut tellus euismod molestie vitae vehicula turpis.</p>
        <span class="pill">learn more</span>
      </div>
      <div class="prod">
        <svg width="22" height="22" viewBox="0 0 22 22"><path d="M3 19L17 5" stroke="#7a8aa0" stroke-width="3"/><path d="M3 3l16 16" stroke="#2f5f9e" stroke-width="3"/><circle cx="18" cy="4" r="3" fill="none" stroke="#7a8aa0" stroke-width="2"/></svg>
        <div class="prod-title">Electronic Lodgement (E-App) and Application Tracking</div>
        <p>Praesent auctor est ut lectus pharetra ut pretium lacus semper.</p>
        <span class="pill">learn more</span>
      </div>
      <div class="prod">
        <svg width="22" height="22" viewBox="0 0 22 22"><rect x="2" y="1" width="14" height="18" fill="#fff" stroke="#999"/><circle cx="12" cy="12" r="5" fill="#cfe0f2" stroke="#556" stroke-width="1.5"/><path d="M15.5 15.5l5 5" stroke="#556" stroke-width="2.5"/></svg>
        <div class="prod-title">Mortgage Product Search and Compare</div>
        <p>Lorem ipsum dolor sit amet, consectetur adipiscing elit. Curabitur ligula ipsum, dapibus.</p>
        <span class="pill">learn more</span>
      </div>

      <div class="sec-head"><h2 class="sec-title">Latest News &amp; Articles</h2></div>
      <div class="news">
        <h3>Quillmere Names New GM</h3>
        <div class="date">Thursday, December 3, 2009 at 3:31PM</div>
        <p>Quillmere has appointed Dalton Meers as the company’s new general manager.</p>
        <p>Mr Meers, who has been a part of the Quillmere group since its inception, has held the position of business manager for the past few years.</p>
        <div class="right"><span class="pill">read more</span></div>
      </div>

      <div class="sec-head"><h2 class="sec-title">Poll</h2></div>
      <div class="poll">
        <p>Quillmere has appointed Dalton Meers as the company’s new general manager?</p>
        <div style="margin-top:4px">
          <label><span class="radio"></span>Best</label>
          <label><span class="radio"></span>Better</label>
          <label><span class="radio"></span>Worst</label>
        </div>
        <span class="pill" style="margin:8px 0 0 8px">submit</span>
      </div>
    </aside>
  </div>

  <footer class="footer">
    <div class="office"><b>Office Location:</b> Level 9 48 Harlow Street Northbay NSW 2071 &nbsp;|&nbsp; <b>Sales:</b> 02 9000 4182 &nbsp;|&nbsp; <b>Support:</b> 1300 555 274</div>
    <div class="links">Sales Platform | e-app | Product Engine | Calculations | Commissions | Messaging | IT Services | Support | Company | News | Contact</div>
    <div class="copy">© 2009, Quillmere Group Inc. All rights reserved.</div>
  </footer>
</div>
</body>
</html>
```